We need a graphic design for a new division called Tally Works. KTR Tally Works offers businesses savings on their Print costs (as in Photocopier and computer printers), Telephony (savings on telephone costs - landline and mobile), Savings on Energy including Electricity and Solar. We would like to use the colours Black, Magenta, Yellow and Cyan. I've uploaded one of our current logos.

```html
<!DOCTYPE html>
<html lang="en">
<head>
<meta charset="utf-8">
<title>KTR Tally Works – Savings Solutions</title>
<link rel="stylesheet" href="https://fonts.googleapis.com/css2?family=Source+Sans+3:wght@400&display=swap">
<style>
  :root {
    --paper: #ffffff;
    --frame: #c9c9c9;
    --ink: #111111;
    --cyan: #1f8fc6;
    --magenta: #d9398f;
    --yellow: #fde11b;
    --black: #151515;
    --mist: #e6e6e6;
    --logo-grey: #3a3a3a;
    --band-shadow: rgba(0, 0, 0, 0.18);
  }
  * { box-sizing: border-box; margin: 0; padding: 0; }
  html, body {
    width: 1200px;
    height: 1000px;
    overflow: hidden;
    background: var(--paper);
  }
  .poster {
    position: relative;
    width: 1200px;
    height: 1000px;
    background: var(--paper);
    border: 2px solid var(--frame);
    font-family: "Source Sans 3", "Myriad Pro", Arial, sans-serif;
    overflow: hidden;
  }
  .corner-pattern {
    position: absolute;
    right: 0;
    top: 0;
    width: 290px;
    height: 240px;
    background: radial-gradient(ellipse at 100% 0%, var(--mist) 0%, #f1f1f1 55%, rgba(255,255,255,0) 80%);
  }
  .headline {
    position: absolute;
    top: 52px;
    left: 0;
    width: 100%;
    text-align: center;
    font-size: 66px;
    font-weight: 400;
    color: var(--ink);
    letter-spacing: 0.5px;
  }
  .service-band {
    position: absolute;
    height: 180px;
    display: flex;
    align-items: center;
    box-shadow: -6px 10px 14px var(--band-shadow);
  }
  .service-band--print  { left: 40px;  top: 170px; width: 850px; background: var(--cyan); }
  .service-band--phone  { left: 167px; top: 398px; width: 843px; background: var(--magenta); }
  .service-band--energy { left: 40px;  top: 637px; width: 860px; background: var(--yellow); }

  .service-icons {
    display: flex;
    align-items: center;
    gap: 22px;
    padding-left: 44px;
  }
  .service-icons svg { display: block; filter: drop-shadow(3px 4px 3px rgba(0,0,0,0.3)); }
  .service-label {
    font-size: 36px;
    line-height: 1.35;
    letter-spacing: 0.3px;
  }
  .service-band--print .service-label  { color: #ffffff; margin-left: 30px; }
  .service-band--phone .service-label  { color: #ffffff; margin-left: 28px; }
  .service-band--energy .service-label { color: var(--ink); margin-left: 42px; }

  .band-accent {
    position: absolute;
  }
  .band-accent--ink-drops {
    left: 830px; top: 172px; width: 145px; height: 175px;
    background: linear-gradient(160deg, var(--black) 0%, var(--magenta) 35%, var(--yellow) 65%, var(--cyan) 100%);
    border-radius: 40% 60% 50% 50%;
    opacity: 0.9;
  }
  .band-accent--coins {
    left: 1008px; top: 395px; width: 172px; height: 200px;
    background: linear-gradient(135deg, var(--black) 0%, var(--yellow) 35%, var(--cyan) 60%, var(--magenta) 100%);
    border-radius: 50%;
    opacity: 0.9;
  }
  .band-accent--bursts {
    left: 875px; top: 630px; width: 160px; height: 200px;
    background: linear-gradient(150deg, var(--magenta) 0%, var(--black) 35%, var(--cyan) 65%, var(--yellow) 100%);
    border-radius: 45%;
    opacity: 0.9;
  }

  .client-mark {
    position: absolute;
    left: 0;
    top: 900px;
    width: 100%;
    display: flex;
    justify-content: center;
    align-items: center;
    gap: 14px;
  }
  .client-mark__dot {
    width: 26px;
    height: 26px;
    border-radius: 50%;
    background: var(--logo-grey);
  }
  .client-mark__name {
    font-size: 34px;
    font-weight: 400;
    color: var(--logo-grey);
  }
</style>
</head>
<body>
<main class="poster">
  <div class="corner-pattern" role="img" aria-label="Faint grey curved grid decoration"></div>

  <h1 class="headline">KTR Tally Works</h1>

  <section class="service-band service-band--print">
    <div class="service-icons">
      <svg width="140" height="110" viewBox="0 0 140 110" aria-label="Photocopier icon" role="img">
        <rect x="2" y="22" width="96" height="72" rx="8" fill="#fff"/>
        <rect x="12" y="30" width="54" height="18" rx="4" fill="var(--cyan)"/>
        <circle cx="22" cy="39" r="4" fill="#fff"/>
        <rect x="30" y="34" width="14" height="10" rx="2" fill="#fff"/>
        <rect x="2" y="56" width="96" height="5" fill="var(--cyan)"/>
        <rect x="2" y="74" width="96" height="5" fill="var(--cyan)"/>
        <rect x="40" y="84" width="20" height="4" fill="var(--cyan)"/>
        <line x1="106" y1="50" x2="136" y2="40" stroke="#fff" stroke-width="5"/>
        <line x1="106" y1="62" x2="136" y2="56" stroke="#fff" stroke-width="5"/>
      </svg>
      <svg width="104" height="110" viewBox="0 0 104 110" aria-label="Printer icon" role="img">
        <path d="M26 4h40l14 14v26H26z" fill="#fff"/>
        <rect x="4" y="44" width="96" height="44" rx="6" fill="#fff"/>
        <rect x="20" y="66" width="64" height="40" fill="#fff" stroke="var(--cyan)" stroke-width="5"/>
        <rect x="32" y="78" width="40" height="5" fill="var(--cyan)"/>
        <rect x="32" y="90" width="40" height="5" fill="var(--cyan)"/>
      </svg>
    </div>
    <p class="service-label">Savings on Print and<br>Photocopier Costs</p>
  </section>
  <div class="band-accent band-accent--ink-drops" role="img" aria-label="Splash of cyan, magenta, yellow and black ink drops"></div>

  <section class="service-band service-band--phone">
    <div class="service-icons">
      <svg width="76" height="124" viewBox="0 0 76 124" aria-label="Mobile phone icon" role="img">
        <rect x="2" y="2" width="72" height="120" rx="12" fill="#fff"/>
        <rect x="10" y="18" width="56" height="84" fill="var(--magenta)"/>
        <circle cx="38" cy="60" r="19" fill="#fff"/>
        <path d="M33 50l14 10-14 10z" fill="var(--magenta)"/>
        <rect x="28" y="108" width="20" height="5" rx="2" fill="var(--magenta)"/>
      </svg>
      <svg width="130" height="124" viewBox="0 0 130 124" aria-label="Desk telephone icon" role="img">
        <rect x="2" y="2" width="30" height="120" rx="10" fill="#fff"/>
        <rect x="40" y="8" width="88" height="110" rx="8" fill="#fff"/>
        <rect x="52" y="18" width="64" height="18" rx="3" fill="var(--magenta)"/>
        <g fill="var(--magenta)">
          <rect x="52" y="46" width="16" height="12"/><rect x="76" y="46" width="16" height="12"/><rect x="100" y="46" width="16" height="12"/>
          <rect x="52" y="64" width="16" height="12"/><rect x="76" y="64" width="16" height="12"/><rect x="100" y="64" width="16" height="12"/>
          <rect x="52" y="82" width="16" height="12"/><rect x="76" y="82" width="16" height="12"/><rect x="100" y="82" width="16" height="12"/>
          <rect x="52" y="100" width="16" height="10"/><rect x="76" y="100" width="16" height="10"/><rect x="100" y="100" width="16" height="10"/>
        </g>
      </svg>
    </div>
    <p class="service-label">Savings on Telephone<br>Costs - Landline and Mobile</p>
  </section>
  <div class="band-accent band-accent--coins" role="img" aria-label="Cluster of coloured dollar coins"></div>

  <section class="service-band service-band--energy">
    <div class="service-icons">
      <svg width="130" height="124" viewBox="0 0 130 124" aria-label="Solar panel and sun icon" role="img">
        <circle cx="86" cy="30" r="18" fill="#fff"/>
        <g stroke="#fff" stroke-width="4">
          <line x1="86" y1="0" x2="86" y2="8"/><line x1="116" y1="30" x2="108" y2="30"/>
          <line x1="107" y1="9" x2="101" y2="15"/><line x1="65" y1="9" x2="71" y2="15"/>
          <line x1="107" y1="51" x2="101" y2="45"/>
        </g>
        <path d="M4 60l80 12-14 40L-2 100z" fill="#fff" transform="translate(6 0)"/>
        <g stroke="var(--yellow)" stroke-width="4">
          <line x1="30" y1="64" x2="22" y2="104"/><line x1="56" y1="68" x2="48" y2="108"/>
          <line x1="8" y1="80" x2="86" y2="92"/>
        </g>
        <rect x="40" y="108" width="6" height="14" fill="#fff"/>
      </svg>
      <svg width="80" height="124" viewBox="0 0 80 124" aria-label="Light bulb icon" role="img">
        <path d="M40 2a36 36 0 0 0-22 64c6 5 8 10 8 18h28c0-8 2-13 8-18A36 36 0 0 0 40 2z" fill="#fff"/>
        <path d="M40 14a24 24 0 0 0-14 43c5 4 7 9 8 15h12c1-6 3-11 8-15A24 24 0 0 0 40 14z" fill="var(--yellow)"/>
        <rect x="26" y="90" width="28" height="6" rx="2" fill="#fff"/>
        <rect x="26" y="100" width="28" height="6" rx="2" fill="#fff"/>
        <rect x="30" y="110" width="20" height="8" rx="3" fill="#fff"/>
      </svg>
    </div>
    <p class="service-label">Savings on Energy Electricity<br>and Solar</p>
  </section>
  <div class="band-accent band-accent--bursts" role="img" aria-label="Cluster of coloured starbursts"></div>

  <footer class="client-mark">
    <span class="client-mark__dot"></span>
    <span class="client-mark__name">Harbour Print Services</span>
  </footer>
</main>
</body>
</html>
```